Update Law Firm Website

Update law firm website pages, add pages for employees. Current website looks stale. www.vantholmlegal.example

Target Market(s)

Personal injury clients

Industry/Entity Type

Legal

Number of Pages Required

5+ page

Font styles to use
Serif

Requirements
Must have
• User friendly and engaging design
Nice to have
• ?
Should not have
• scales of justice, law books,

```html
<!DOCTYPE html>
<html lang="en">
<head>
<meta charset="utf-8">
<title>The Law Office of Daniel R. Vantholm</title>
<link rel="stylesheet" href="https://fonts.googleapis.com/css2?family=Roboto+Slab:wght@400;700&family=Raleway:wght@400;600;700&display=swap">
<style>
:root{
  --navy:#0d2f6b;
  --navy-dark:#0a2456;
  --navy-deep:#081c44;
  --ink:#222;
  --muted:#555;
  --line:#ddd;
  --paper:#fff;
  --soft:#f1f1f1;
  --nav-active:#5a5a5a;
}
*{box-sizing:border-box;margin:0;padding:0}
html,body{width:1200px;height:3681px;overflow:hidden}
body{position:relative;font-family:'Raleway',sans-serif;color:var(--ink);background:var(--paper)}
.abs{position:absolute}
.serif{font-family:'Roboto Slab',serif}
section,header,nav,footer{position:absolute;left:0;width:1200px}

/* header */
.site-header{top:0;height:84px;background:#fff}
.brand{left:100px;top:16px;font-family:'Roboto Slab',serif;color:var(--navy);line-height:1}
.brand .small{font-size:19px;display:block}
.brand .big{font-size:24px;font-weight:700;display:block;margin-top:3px}
.contact-item{top:22px;display:flex;align-items:center;gap:12px;font-size:15px;color:var(--ink)}
.contact-item .dot{width:34px;height:34px;border-radius:50%;background:var(--navy);display:flex;align-items:center;justify-content:center}

/* nav */
.main-nav{top:84px;height:58px;background:var(--navy)}
.main-nav a{position:absolute;top:0;height:58px;line-height:58px;color:#fff;font-size:15px;font-weight:700;text-decoration:none;text-align:center}
.main-nav .active{background:var(--nav-active)}

/* hero */
.hero{top:142px;height:470px}
.hero-photo{position:absolute;inset:0;background:linear-gradient(90deg,#9fc2d8 0%,#c9dbe6 35%,#e3e6ea 60%,#bfc4cc 100%)}
.hero h1{position:absolute;left:100px;top:190px;font-family:'Roboto Slab',serif;color:#fff;font-size:37px;font-weight:700;letter-spacing:1px;text-shadow:0 2px 4px rgba(0,0,0,.3)}
.hero p{position:absolute;left:100px;top:238px;font-family:'Roboto Slab',serif;color:#fff;font-size:20px;font-weight:700;letter-spacing:1px;text-shadow:0 2px 4px rgba(0,0,0,.3)}
.dots{position:absolute;display:flex;gap:8px}
.dots span{width:11px;height:11px;border-radius:50%;background:#fff;opacity:.8}
.dots span.on{background:var(--navy);opacity:1;border:2px solid #fff}

/* about */
.about{top:612px;height:348px;background:#fff}
.about h2{position:absolute;left:100px;top:40px;font-family:'Roboto Slab',serif;font-weight:400;font-size:34px;color:#333}
.about h2 b{color:var(--navy);font-weight:400}
.underline{position:absolute;height:2px;background:var(--navy)}
.portrait{position:absolute;left:100px;top:112px;width:175px;height:185px;border:4px solid #e2e2e2;background:linear-gradient(180deg,#8a8f99,#3b3f48)}
.about-text{position:absolute;left:295px;top:106px;width:540px;font-size:13.3px;line-height:22px;color:#444;text-align:justify}
.btn{position:absolute;background:var(--navy);color:#fff;font-size:15px;text-align:center;font-family:'Raleway',sans-serif}
.accred h3{position:absolute;left:865px;top:46px;font-family:'Roboto Slab',serif;font-weight:400;font-size:24px;color:var(--navy)}
.badge-box{position:absolute;left:865px;width:232px;background:#f4f4f4;border:1px solid #e6e6e6;display:flex;align-items:center;justify-content:center}

/* practice */
.practice{top:960px;height:508px;background:linear-gradient(180deg,#1d3f7a 0%,#0d2f6b 60%,#0a2456 100%)}
.section-title{position:absolute;left:0;width:1200px;text-align:center;font-family:'Roboto Slab',serif;font-size:34px;font-weight:400}
.practice .section-title{color:#fff;top:40px}
.title-rule{position:absolute;left:540px;width:120px;height:2px}
.card{position:absolute;top:140px;width:232px;height:273px;background:#fff;text-align:center}
.card .icon{position:absolute;left:58px;top:20px;width:116px;height:116px;border-radius:50%;background:#f0f0f0;display:flex;align-items:center;justify-content:center}
.card h4{position:absolute;top:160px;width:100%;font-size:18px;font-weight:600;color:var(--navy)}
.card .rule{position:absolute;left:20px;right:20px;top:188px;height:1px;background:#ddd}
.card p{position:absolute;top:196px;left:16px;right:16px;font-size:13px;line-height:20px;color:#555}
.card .plus{position:absolute;left:94px;bottom:-22px;width:44px;height:44px;border-radius:50%;background:#444;color:#fff;font-size:22px;line-height:36px}

/* why */
.why{top:1468px;height:498px;background:#f4f4f4;overflow:hidden}
.why .section-title{top:40px;color:var(--navy)}
.hub{position:absolute;left:450px;top:316px;width:300px;height:300px;border-radius:50%;background:#fff;box-shadow:0 0 30px rgba(0,0,0,.18);text-align:center;font-family:'Roboto Slab',serif;color:var(--navy)}
.hub .s{display:block;margin-top:82px;font-size:19px}
.hub .b{display:block;font-size:21px;font-weight:700}
.feat{position:absolute;width:82px;height:82px;border-radius:50%;background:var(--navy);border:5px solid #fff;box-shadow:0 0 0 2px var(--navy);display:flex;align-items:center;justify-content:center}
.feat-label{position:absolute;font-family:'Roboto Slab',serif;font-size:22px;color:var(--navy);line-height:24px}

/* testimonials */
.testimonials{top:1966px;height:427px;background:linear-gradient(160deg,#2c4677 0%,#1c3566 50%,#132a57 100%)}
.testimonials .section-title{top:34px;color:#fff}
.quote{position:absolute;top:140px;width:300px;text-align:center;color:#fff}
.avatar{width:120px;height:120px;margin:0 auto;border-radius:50%;border:5px solid #c9d1de;background:linear-gradient(180deg,#a9b4c4,#5e6b80)}
.quote .q{display:flex;gap:10px;margin-top:26px;text-align:left}
.quote .mark{font-family:'Roboto Slab',serif;font-size:60px;line-height:44px;color:#c9d1de}
.quote p{font-size:12.5px;font-style:italic;line-height:18px}
.quote .who{margin-top:12px;font-size:13.5px;font-weight:700}
.arrow{position:absolute;top:210px;width:38px;height:38px;border-radius:50%;background:#8d97a8;display:flex;align-items:center;justify-content:center}

/* news */
.news{top:2393px;height:539px;background:#ededed}
.news .section-title{top:38px;color:#333}
.news-card{position:absolute;top:115px;width:318px;height:327px;background:#fff;box-shadow:0 1px 4px rgba(0,0,0,.12)}
.news-card .ph{height:180px}
.news-card .date{position:absolute;left:16px;top:198px;width:34px;height:44px;background:var(--navy);color:#fff;text-align:center;font-size:15px;font-weight:700;line-height:26px}
.news-card .date small{display:block;font-size:8px;line-height:10px;background:#fff;color:var(--navy);margin:0 3px}
.news-card h5{position:absolute;left:62px;top:198px;font-size:13.5px;font-weight:600;color:#333}
.news-card .meta{position:absolute;left:62px;top:222px;font-size:12px;color:#777}
.news-card p{position:absolute;left:62px;right:12px;top:248px;font-size:12px;line-height:18px;color:#555}

/* callback */
.callback{top:2932px;height:286px;background:var(--navy)}
.callback h2{position:absolute;left:100px;top:40px;font-family:'Roboto Slab',serif;font-size:36px;font-weight:400;color:#fff;line-height:44px}
.callback .lead{position:absolute;left:100px;top:146px;width:260px;font-size:12.5px;line-height:20px;color:#dfe5ef}
.callback .form-label{position:absolute;left:460px;top:50px;font-size:14px;font-weight:700;color:#fff}
.field{position:absolute;height:42px;background:#fff;font-size:13px;color:#888;padding:12px 12px}

/* footer */
.site-footer{top:3218px;height:463px;background:linear-gradient(180deg,#2b1c12 0%,#1c140f 50%,#110c09 100%)}
.f-col{position:absolute;top:40px;width:300px;text-align:center;color:#fff;font-size:13px}
.f-col svg{display:block;margin:0 auto 30px}
.f-rule{position:absolute;top:60px;height:1px;background:#777}
.f-brand{position:absolute;left:0;width:1200px;top:160px;text-align:center;font-family:'Roboto Slab',serif;color:#fff;line-height:1}
.f-brand .small{font-size:21px;display:block}
.f-brand .big{font-size:26px;font-weight:700;display:block;margin-top:4px}
.rating-badge{position:absolute;left:500px;top:248px;width:200px;height:90px;background:#fff;border-radius:4px}
.copyright{position:absolute;left:0;top:387px;width:1200px;height:76px;border-top:1px solid #444;background:#0e0a08}
.copyright p{position:absolute;left:100px;top:28px;font-size:13px;color:#ddd}
.social{position:absolute;top:19px;width:38px;height:38px;border-radius:50%}
</style>
</head>
<body>

<header class="site-header">
  <div class="abs brand"><span class="small">THE LAW OFFICE OF</span><span class="big">DANIEL R. VANTHOLM</span></div>
  <div class="abs contact-item" style="left:718px">
    <span class="dot"><svg width="16" height="16" viewBox="0 0 24 24"><path fill="#fff" d="M6.6 10.8a15 15 0 0 0 6.6 6.6l2.2-2.2c.3-.3.7-.4 1-.2 1.1.4 2.3.6 3.6.6.6 0 1 .4 1 1V20c0 .6-.4 1-1 1C10.6 21 3 13.4 3 4c0-.6.4-1 1-1h3.5c.6 0 1 .4 1 1 0 1.3.2 2.5.6 3.6.1.3 0 .7-.2 1z"/></svg></span>
    <span>(555) 010-4420</span>
  </div>
  <div class="abs contact-item" style="left:920px">
    <span class="dot"><svg width="16" height="16" viewBox="0 0 24 24"><path fill="#fff" d="M3 6h18v12H3z"/><path d="M3 6l9 7 9-7" stroke="#0d2f6b" stroke-width="2" fill="none"/></svg></span>
    <span style="font-size:13px">info@vantholmlegal.example</span>
  </div>
</header>

<nav class="main-nav">
  <a class="active" style="left:98px;width:118px">Home</a>
  <a style="left:283px;width:120px">About Us</a>
  <a style="left:500px;width:150px">Practice Areas ▾</a>
  <a style="left:730px;width:140px">Testimonials</a>
  <a style="left:1030px;width:126px">Contact Us</a>
</nav>

<section class="hero">
  <div class="hero-photo" role="img" aria-label="Photo of a person with an arm in a sling in a bright hospital corridor"></div>
  <h1>AFFORDABLE &amp; ESSENTIAL</h1>
  <p>LEGAL ADVOCATE FOR YOUR INJURY CLAIM</p>
  <div class="dots" style="left:108px;top:444px"><span class="on"></span><span></span><span></span><span></span></div>
</section>

<section class="about">
  <h2>About The Law Office of <b>Daniel R. Vantholm</b></h2>
  <div class="underline" style="left:100px;top:96px;width:700px;background:#ccc;height:1px"></div>
  <div class="underline" style="left:100px;top:95px;width:220px"></div>
  <div class="portrait" role="img" aria-label="Portrait photo of the attorney"></div>
  <p class="about-text">When you are hit by a fatigued driver of a tractor-trailer or you suffer a fatal stroke because of a delayed diagnosis by a physician, the consequences can include staggering medical bills, debilitating pain and permanent disability. While overcoming the emotional, physical and financial hardships associated with a serious injury always present serious challenges, incidents resulting in substantial injuries can be even more traumatic when they are caused by the negligent.</p>
  <div class="btn" style="left:295px;top:260px;width:137px;height:38px;line-height:38px">Read More</div>
  <div class="accred">
    <h3>Our Accreditations</h3>
    <div class="underline" style="left:865px;top:90px;width:232px;background:#ccc;height:1px"></div>
    <div class="badge-box" style="top:112px;height:75px"><svg width="160" height="36"><rect width="160" height="36" rx="4" fill="#caa448"/></svg></div>
    <div class="badge-box" style="top:198px;height:125px"><svg width="108" height="108"><circle cx="54" cy="54" r="52" fill="#c9a240"/><circle cx="54" cy="54" r="42" fill="#0d2f6b"/></svg></div>
  </div>
</section>

<section class="practice">
  <h2 class="section-title">Our Practice Areas</h2>
  <div class="title-rule" style="top:94px;background:#fff"></div>
  <div class="card" style="left:98px">
    <div class="icon"><svg width="60" height="60" viewBox="0 0 60 60"><circle cx="22" cy="10" r="6" fill="#0d2f6b"/><path d="M18 18h8v16h12l6 14h-5l-4-9H18z" fill="#0d2f6b"/><circle cx="20" cy="42" r="12" fill="none" stroke="#0d2f6b" stroke-width="3"/></svg></div>
    <h4>Personal Injury</h4><div class="rule"></div>
    <p>Whether you fall on a wet floor in a local grocery store or...</p>
    <div class="plus">+</div>
  </div>
  <div class="card" style="left:355px">
    <div class="icon"><svg width="64" height="50" viewBox="0 0 64 50"><path d="M4 34l10-22h18l10 14h14v10H4z" fill="#0d2f6b"/><circle cx="16" cy="40" r="6" fill="#0d2f6b"/><circle cx="48" cy="40" r="6" fill="#0d2f6b"/></svg></div>
    <h4>Auto Accident</h4><div class="rule"></div>
    <p>When motorists drive the streets and highways of...</p>
    <div class="plus">+</div>
  </div>
  <div class="card" style="left:610px">
    <div class="icon"><svg width="64" height="60" viewBox="0 0 64 60"><circle cx="44" cy="20" r="12" fill="none" stroke="#0d2f6b" stroke-width="6" stroke-dasharray="5 3"/><circle cx="44" cy="44" r="8" fill="none" stroke="#0d2f6b" stroke-width="5" stroke-dasharray="4 3"/><circle cx="14" cy="14" r="5" fill="#0d2f6b"/><path d="M12 20l6 14-8 10M18 34l10 4" stroke="#0d2f6b" stroke-width="4" fill="none"/></svg></div>
    <h4>Construction Injuries</h4><div class="rule"></div>
    <p>The construction industry remains one of the most...</p>
    <div class="plus">+</div>
  </div>
  <div class="card" style="left:870px">
    <div class="icon"><svg width="60" height="60" viewBox="0 0 60 60"><circle cx="18" cy="10" r="6" fill="#0d2f6b"/><rect x="12" y="18" width="12" height="36" fill="#0d2f6b"/><circle cx="40" cy="14" r="6" fill="#0d2f6b"/><rect x="34" y="22" width="12" height="32" fill="#0d2f6b"/><path d="M50 28v26" stroke="#0d2f6b" stroke-width="3"/></svg></div>
    <h4>Medical Malpractice</h4><div class="rule"></div>
    <p>When patients seek medical treatment, there is a common...</p>
    <div class="plus">+</div>
  </div>
</section>

<section class="why">
  <h2 class="section-title">Why Choose Us</h2>
  <div class="title-rule" style="top:94px;background:var(--navy)"></div>
  <svg class="abs" style="left:0;top:0" width="1200" height="498">
    <line x1="588" y1="280" x2="588" y2="318" stroke="#666" stroke-width="1.5"/>
    <line x1="410" y1="330" x2="465" y2="355" stroke="#666" stroke-width="1.5"/>
    <line x1="778" y1="330" x2="728" y2="355" stroke="#666" stroke-width="1.5"/>
  </svg>
  <div class="hub"><span class="s">THE LAW OFFICE OF</span><span class="b">DANIEL R. VANTHOLM</span></div>
  <div class="feat-label" style="left:488px;top:134px;width:200px;text-align:center">Personalized<br>Attention</div>
  <div class="feat" style="left:547px;top:190px"><svg width="38" height="38" viewBox="0 0 38 38"><circle cx="19" cy="19" r="15" fill="none" stroke="#fff" stroke-width="2.5"/><circle cx="19" cy="15" r="4" fill="#fff"/><path d="M12 27c1-5 13-5 14 0z" fill="#fff"/></svg></div>
  <div class="feat-label" style="left:150px;top:332px;width:160px;text-align:right">Our<br>Commitment</div>
  <div class="feat" style="left:320px;top:312px"><svg width="44" height="32" viewBox="0 0 44 32"><path d="M2 12l10-8 8 4 6-4 16 10-10 12-6-4-6 4-8-6z" fill="#fff"/></svg></div>
  <div class="feat" style="left:778px;top:312px"><svg width="42" height="42" viewBox="0 0 42 42"><circle cx="21" cy="21" r="17" fill="none" stroke="#fff" stroke-width="3"/><circle cx="21" cy="21" r="10" fill="none" stroke="#fff" stroke-width="3"/><circle cx="21" cy="21" r="3" fill="#fff"/><path d="M21 21L38 4" stroke="#fff" stroke-width="3"/></svg></div>
  <div class="feat-label" style="left:878px;top:314px;width:200px">Focused On<br>Results</div>
</section>

<section class="testimonials">
  <h2 class="section-title">What Our Clients &nbsp;Say</h2>
  <div class="title-rule" style="top:88px;background:#fff"></div>
  <div class="arrow" style="left:60px"><svg width="14" height="14"><path d="M10 2L4 7l6 5" stroke="#fff" stroke-width="2.5" fill="none"/></svg></div>
  <div class="arrow" style="left:1102px"><svg width="14" height="14"><path d="M4 2l6 5-6 5" stroke="#fff" stroke-width="2.5" fill="none"/></svg></div>
  <div class="quote" style="left:110px">
    <div class="avatar" role="img" aria-label="Client portrait photo"></div>
    <div class="q"><span class="mark">“</span><p>Lorem ipsum dolor sit amet, consectetuer adipiscing elit, sed diam nonummy. Lorem ipsum dolor sit amet, consectetuer adipiscing elit.</p></div>
    <div class="who">- Consectetue Radipiscing</div>
  </div>
  <div class="quote" style="left:440px">
    <div class="avatar" role="img" aria-label="Client portrait photo"></div>
    <div class="q"><span class="mark">“</span><p>Lorem ipsum dolor sit amet, consectetuer adipiscing elit, sed diam nonummy. Lorem ipsum dolor sit amet, consectetuer adipiscing elit.</p></div>
    <div class="who">- Diam Nonummy</div>
  </div>
  <div class="quote" style="left:770px">
    <div class="avatar" role="img" aria-label="Client portrait photo"></div>
    <div class="q"><span class="mark">“</span><p>Lorem ipsum dolor sit amet, consectetuer adipiscing elit, sed diam nonummy. Lorem ipsum dolor sit amet, consectetuer adipiscing elit.</p></div>
    <div class="who">- Dolor Sitamet</div>
  </div>
</section>

<section class="news">
  <h2 class="section-title">Latest News</h2>
  <div class="title-rule" style="top:92px;background:var(--navy)"></div>
  <div class="news-card" style="left:98px">
    <div class="ph" role="img" aria-label="Photo of an elderly couple meeting with an advisor" style="background:linear-gradient(135deg,#d9c9b4,#7e8fa6)"></div>
    <div class="date">24<small>DEC</small></div>
    <h5>Lorem ipsum dolor sit amet,</h5>
    <div class="meta">by admin &nbsp;|&nbsp; in news, business</div>
    <p>Ut wisi enim ad minim veniam, quisvero exerci tation ullamcorper.</p>
  </div>
  <div class="news-card" style="left:440px">
    <div class="ph" role="img" aria-label="Photo of a distressed woman holding her head" style="background:linear-gradient(135deg,#b9c4cf,#6f7d8e)"></div>
    <div class="date">24<small>DEC</small></div>
    <h5>Duis autem vel eum iriure dolo,</h5>
    <div class="meta">by admin &nbsp;|&nbsp; in news, business</div>
    <p>Ut wisi enim ad minim veniam, quisvero exerci tation ullamcorper.</p>
  </div>
  <div class="news-card" style="left:782px">
    <div class="ph" role="img" aria-label="Photo of a patient in a neck brace at a hospital" style="background:linear-gradient(135deg,#8fa3b8,#dbe4ec)"></div>
    <div class="date">24<small>DEC</small></div>
    <h5>Vel illum dolore eu feugiat nulla</h5>
    <div class="meta">by admin &nbsp;|&nbsp; in news, business</div>
    <p>Ut wisi enim ad minim veniam, quisvero exerci tation ullamcorper.</p>
  </div>
  <div class="dots" style="left:586px;top:473px"><span class="on" style="border:none;width:10px;height:10px"></span><span style="background:#fff;border:1px solid #aaa;width:10px;height:10px"></span></div>
</section>

<section class="callback">
  <h2>Request<br>A Call Back.</h2>
  <p class="lead">Duis autem vel eum iriure dolormi opi inmoki hendi rerit in vulpu tatemi velitm essemol mo molestiel conseqb ual, velmi illum dolor eokf no atn nulla more facilisis...</p>
  <div class="form-label">Please fill up bellow form</div>
  <div class="field" style="left:460px;top:82px;width:308px">Name</div>
  <div class="field" style="left:792px;top:82px;width:308px">Email</div>
  <div class="field" style="left:460px;top:134px;width:308px">Phone</div>
  <div class="field" style="left:792px;top:134px;width:308px">Message</div>
  <div class="btn" style="left:460px;top:190px;width:162px;height:42px;line-height:42px;background:#fff;color:var(--navy);font-weight:700">Submit</div>
</section>

<footer class="site-footer" role="img" aria-label="Dark photo of a desk with a laptop and papers behind the footer">
  <div class="f-col" style="left:160px">
    <svg width="20" height="24" viewBox="0 0 20 24"><path d="M10 1a7 7 0 0 0-7 7c0 6 7 14 7 14s7-8 7-14a7 7 0 0 0-7-7z" fill="none" stroke="#fff" stroke-width="1.8"/><circle cx="10" cy="8" r="2.5" fill="#fff"/></svg>
    Suite 1500 Harbor Ave #1207 Eastfield, PA 19000
  </div>
  <div class="f-rule" style="left:500px;width:90px"></div>
  <div class="f-rule" style="left:655px;width:90px"></div>
  <div class="f-col" style="left:470px">
    <svg width="22" height="22" viewBox="0 0 24 24"><path fill="none" stroke="#fff" stroke-width="1.6" d="M6.6 10.8a15 15 0 0 0 6.6 6.6l2.2-2.2c.3-.3.7-.4 1-.2 1.1.4 2.3.6 3.6.6.6 0 1 .4 1 1V20c0 .6-.4 1-1 1C10.6 21 3 13.4 3 4c0-.6.4-1 1-1h3.5c.6 0 1 .4 1 1 0 1.3.2 2.5.6 3.6.1.3 0 .7-.2 1z"/></svg>
    Phone: (555) 010-4300
  </div>
  <div class="f-col" style="left:790px">
    <svg width="22" height="22" viewBox="0 0 24 24"><path d="M2 11L22 2l-9 20-2-9z" fill="none" stroke="#fff" stroke-width="1.6"/></svg>
    Email: info@vantholmlegal.example
  </div>
  <div class="f-brand"><span class="small">THE LAW OFFICE OF</span><span class="big">DANIEL R. VANTHOLM</span></div>
  <div class="rating-badge"></div>
  <div class="copyright">
    <p>Copyright © 2017 The Law Office Of Daniel R. Vantholm. All Rights Reserved.</p>
    <span class="social" style="left:910px;background:#3b5a9a"></span>
    <span class="social" style="left:960px;background:#1b7ab0"></span>
    <span class="social" style="left:1010px;background:#3aa0d8"></span>
    <span class="social" style="left:1060px;background:#d4483a"></span>
  </div>
</footer>

</body>
</html>
```